Continuing Professional Development Seminars
Power Point Template
• 11 juin 2011 15:52 rubenqol
thanks Velmoro
• 9 juin 2011 11:07 Velmoro
congrats your first project :)
• 9 juin 2011 02:48 tkvolaris
rubenqol - can you please upload a new draft that has the following slides:
1 - The title slide from draft#15 (I think this might be exactly the same in all subsequent drafts)
2 - The content slide from draft#15
3 - The content slide from draft#66
4 - The content slide from draft#68
5 - The last slide from draft#69
6 - The last slide from draft#15
I would like to see both of the end slides in the same draft.
Thanks.
• 7 juin 2011 08:20 tkvolaris
Thank you to all the designers who have submitted designs to date. The quality of the work is outstanding and is making the decision difficult.
I am still considering ALL the designs and will probably make a final decision soon. However, the designs that seem to stand out at the moment include (in no particular order) draft#50/draft#72, draft#15 (and the variations), draft#62 and draft#54.
• 6 juin 2011 06:31 tkvolaris
Draft#15 – can you please make the following changes:
1. Replace the last slide with a variant of the first slide. This new slide should be the same as the first slide, but with the following changes:
• The colours of the main background graphic should be reversed – so that becomes a red graphic with a blue stipe (instead of a blue graphic with a red stripe).
• Change the text - “Welcome to our Presentation” to “Thank you”.
• Change the white text (location and date) to the contact details you currently have on the last slide.
2. Can we try three small variations to the header on the content slides? Firstly, can you make the line under the presentation header about an inch smaller (so that it doesn’t go all the way to the logo). Secondly, can you please do a variant that reverses the logo and the header title (so that the logo is on the right and the presentation title is on the left). Thirdly, can you try a variant that doesn’t have the presentation header at all – only the logo? I would prefer having a look at all three slides to see how it looks. Thanks.
• 2 juin 2011 06:02 tkvolaris
Some of the recent designs have been very good. I particularly like the very bold graphical styles on the front pages whilst I prefer the more minimalist approach to the content slides.
I know that I said previously to try using our logo as a background watermark. However, on second thoughts I don’t think it really works. The watermarks are OK on the first slides, but on the content slides it is very distracting.
So far, my favourite designs are draft#15 and drafts#25-26. However, many of the designs have things I like or don’t like. Specifically,
• Draft#25 and Draft #26 – These designs are very effective. A bold front page and simple content pages. I think we would need to lose the watermarks on the content pages, but otherwise, these designs are on the right track.
• Draft#23 – I like the footer design of each content slide. Very simple and elegant.
• Draft#15 – perhaps my favourite design so far. Good bold first slide. The content slides are also good – maybe a little too busy as the moment?
• Draft#9 and Draft#10 – The first slides in these designs are very good. I like the strong bold designs. The content pages don’t really work – too much graphical background and not enough white space for content. One thing I like about these designs is the reverse colours of the background on the final slides.
Some of the other designs have similar good and bad points. However, I think I would be repeating myself if I discussed each one.
In summary, I like the first slides that are bold and emphasise our brand. The content slides should be simple, elegant and consistent.
• 31 mai 2011 19:56 tkvolaris
When I was looking through other projects on this website, there is one that I found that seems to be very effective. The project name is "Brisk Lanterns PowerPoint Template" and the design is draft#39.
I am not suggesting that I want a copy or a redraft of this design. It is just an example of something that I like.
• 31 mai 2011 19:47 tkvolaris
I like the designs that are creatively using the "swirls" on our logo. The first pages in draft#9 and draft#10 are interesting. I also didn't mind the first page in draft#11 (but note that it has been withdrawn?).
I think the logo needs to be more subtle on the content pages - maybe in the bottom right corner? Also maybe could use the logo as a watermark? Draft#4 uses a watermark, but being in the middle of the page, it might be a little distracting.

```html
<!DOCTYPE html>
<html lang="en">
<head>
<meta charset="utf-8">
<title>ORVEN Presentation Template</title>
<link rel="stylesheet" href="https://fonts.googleapis.com/css2?family=Open+Sans:wght@400;600;700&display=swap">
<style>
  :root {
    --blue: #1d4fa6;
    --blue-deep: #163b8c;
    --blue-bright: #2c6cc4;
    --accent-blue: #1f8ad6;
    --red: #d6222c;
    --ink: #5a5a5a;
    --text-grey: #8a8a8a;
    --rule: #9a9a9a;
    --paper: #ffffff;
    --paper-shade: #ececec;
    --stage-light: #e4e4e4;
    --stage-dark: #a9a9a9;
  }
  * { margin: 0; padding: 0; box-sizing: border-box; }
  html, body { width: 1200px; height: 986px; overflow: hidden; }
  body {
    font-family: "Open Sans", sans-serif;
    background: radial-gradient(ellipse at 50% 45%, var(--stage-light) 0%, #cfcfcf 55%, var(--stage-dark) 100%);
    position: relative;
  }
  .slide {
    position: absolute;
    overflow: hidden;
    background: linear-gradient(180deg, var(--paper) 0%, var(--paper) 55%, var(--paper-shade) 100%);
    box-shadow: 0 2px 6px rgba(0,0,0,0.25);
  }
  .slide-title   { left: 99px;  top: 107px; width: 449px; height: 390px; }
  .slide-content { left: 620px; top: 107px; width: 481px; height: 390px; }
  .slide-image   { left: 99px;  top: 575px; width: 449px; height: 300px; }
  .slide-closing { left: 620px; top: 575px; width: 481px; height: 300px;
    background: radial-gradient(ellipse at 50% 40%, var(--blue-bright) 0%, var(--blue) 55%, var(--blue-deep) 100%); }

  .footer-band {
    position: absolute; left: 0; right: 0; bottom: 0;
    background: linear-gradient(180deg, var(--blue-bright) 0%, var(--blue) 45%, var(--blue-deep) 100%);
  }
  .slide-title .footer-band   { height: 142px; }
  .slide-content .footer-band { height: 70px; }
  .slide-image .footer-band   { height: 48px; }

  .brand {
    display: flex; align-items: center; gap: 6px;
    font-weight: 700; color: var(--blue); letter-spacing: 0.5px;
    white-space: nowrap;
  }
  .brand-dot { border-radius: 50%; background: var(--red); flex: none; }
  .slide-title .brand { position: absolute; left: 26px; top: 36px; font-size: 26px; }
  .slide-title .brand-dot { width: 10px; height: 10px; }

  .welcome { position: absolute; right: 24px; top: 112px; text-align: right; }
  .welcome h1 { font-size: 25px; font-weight: 700; color: var(--accent-blue); line-height: 1.1; }
  .welcome p  { font-size: 19px; color: var(--ink); letter-spacing: 0.3px; line-height: 1.3; }
  .event-line {
    position: absolute; right: 24px; bottom: 28px;
    color: #fff; font-size: 15px;
  }

  .header {
    position: absolute; left: 16px; right: 18px; top: 14px;
    display: flex; align-items: flex-end; gap: 10px;
  }
  .header .brand { font-size: 17px; line-height: 1; }
  .header .brand-dot { width: 7px; height: 7px; }
  .header .title-group { flex: 1; text-align: right; border-bottom: 1px solid var(--rule); padding-bottom: 2px; }
  .header .deck-title { font-size: 12px; color: var(--accent-blue); letter-spacing: 0.3px; }

  .body-copy { position: absolute; font-size: 8.5px; line-height: 1.75; color: var(--text-grey); }
  .slide-content .copy-one { left: 22px; top: 74px; width: 258px; }
  .slide-content .copy-two { left: 22px; top: 168px; width: 258px; }
  .slide-image .copy-one   { left: 40px; top: 190px; width: 370px; }

  .image-box {
    position: absolute;
    border: 1px solid #c4c4c4;
    background: linear-gradient(180deg, #fafafa, #efefef);
    display: flex; align-items: center; justify-content: center;
    font-size: 20px; color: #9c9c9c; letter-spacing: 0.5px;
  }
  .slide-content .image-box { left: 318px; top: 74px; width: 140px; height: 180px; }
  .slide-image .image-box   { left: 54px; top: 54px; width: 346px; height: 118px; }

  .thanks {
    position: absolute; left: 0; right: 0; top: 96px; text-align: center;
    color: #fff; font-size: 20px; letter-spacing: 0.5px;
  }
  .slide-closing .brand {
    position: absolute; left: 50%; transform: translateX(-50%); top: 192px;
    color: #fff; font-size: 20px;
  }
  .slide-closing .brand-dot { width: 8px; height: 8px; background: #fff; }
  .contact {
    position: absolute; left: 0; right: 0; top: 234px; text-align: center;
    color: #dfe7f6; font-size: 7px; line-height: 1.6;
  }
</style>
</head>
<body>

<section class="slide slide-title">
  <div class="footer-band" role="img" aria-label="Decorative blue footer graphic with a red accent"></div>
  <div class="brand"><span class="brand-dot"></span>ORVEN</div>
  <div class="welcome">
    <h1>WELCOME</h1>
    <p>TO OUR PRESENTATION</p>
  </div>
  <p class="event-line">Birmingham, March 25, 2011</p>
</section>

<section class="slide slide-content">
  <div class="footer-band" role="img" aria-label="Decorative blue footer graphic with a red accent"></div>
  <header class="header">
    <div class="brand"><span class="brand-dot"></span>ORVEN</div>
    <div class="title-group"><span class="deck-title">PRESENTATION TITLE</span></div>
  </header>
  <p class="body-copy copy-one">Add your main content here. Keep each point short and clear so the audience can follow along with ease during the session.</p>
  <p class="body-copy copy-two">Use this second block for supporting detail, a short summary or a quote that backs up the key message of the slide.</p>
  <div class="image-box">IMAGE</div>
</section>

<section class="slide slide-image">
  <div class="footer-band" role="img" aria-label="Decorative blue footer graphic with a red accent"></div>
  <header class="header">
    <div class="brand"><span class="brand-dot"></span>ORVEN</div>
    <div class="title-group"><span class="deck-title">PRESENTATION TITLE</span></div>
  </header>
  <div class="image-box">IMAGE</div>
  <p class="body-copy copy-one">Place a brief caption or description of the image above in this area, using two or three lines of plain supporting text for context.</p>
</section>

<section class="slide slide-closing">
  <p class="thanks">THANK YOU</p>
  <div class="brand"><span class="brand-dot"></span>ORVEN</div>
  <p class="contact">12 Harlow Street, Birmingham B1 4QT<br>T: 0121 555 0187 | E: info@orven.example</p>
</section>

</body>
</html>
```